High Quality Business card for Property Management Agency - Super Classy and professional design

High Quality Business card design.

We need a business card designed for our Property Management Agency.
We are located on Sydney's Northern Beaches and manage beautiful properties along the beach and harbor.
We need a design that oozes modern, classy and professional.
I would like it to be double sided with contact details and logo on the front and just the logo on the back.

I need a print ready PDF version of the file as well as an editable photoshop (PSD) version of the file.

Logo and information details attached.

Target Market(s)

Property owners/investors, Male and Female Aged 28-65

Industry/Entity Type

Real Estate

Contact Information for Business Card

Tom Harlow
Tel: 0437 216 590
Email: tom@harlowestates.com.au
Website: www.harlowestates.com.au
Address: Level 2, 17 Kestrel Rd, Wendale NSW 2081

Font styles to use
Sans Serif

Requirements
Must have
• - Logo front and back
• - Business card details listed above and attached
• - Colour
Nice to have
• Sleek and professional

```html
<!DOCTYPE html>
<html lang="en">
<head>
<meta charset="utf-8">
<title>Harlow Estates – Business Card</title>
<link href="https://fonts.googleapis.com/css2?family=Exo+2:wght@400;600;800&display=swap" rel="stylesheet">
<style>
  :root {
    --page: #e6e7e8;
    --card: #ffffff;
    --ink: #1d1d1d;
    --teal: #1f8fa0;
    --photo-sky: #8fc3e6;
    --photo-mid: #c9b8a3;
    --photo-water: #3f93a3;
    --shadow: 0 10px 24px rgba(0,0,0,0.28);
  }
  * { box-sizing: border-box; margin: 0; padding: 0; }
  html, body {
    width: 1071px; height: 1200px; overflow: hidden;
    background: var(--page);
    font-family: "Exo 2", sans-serif;
    color: var(--ink);
  }
  .canvas { position: relative; width: 1071px; height: 1200px; }
  .card {
    position: absolute; left: 186px; width: 700px; height: 400px;
    background: var(--card); box-shadow: var(--shadow); overflow: hidden;
  }
  .card--back { top: 170px; display: flex; align-items: center; justify-content: center; }
  .card--front { top: 630px; display: flex; }

  .brand { display: flex; align-items: center; gap: 22px; }
  .brand__dot { width: 34px; height: 34px; border-radius: 50%; background: var(--teal); }
  .brand__name {
    font-weight: 600; font-size: 62px; letter-spacing: 1px; color: var(--ink);
  }

  .portrait {
    width: 290px; height: 100%;
    background: linear-gradient(180deg, var(--photo-sky) 0%, var(--photo-mid) 45%, var(--photo-water) 100%);
  }
  .details { position: relative; flex: 1; padding: 44px 0 0 34px; }
  .details__name { font-weight: 800; font-size: 24px; }
  .details__phone {
    display: flex; align-items: center; gap: 10px;
    font-weight: 400; font-size: 36px; letter-spacing: 1px; margin-top: 2px;
  }
  .contact-list {
    position: absolute; left: 34px; bottom: 48px; list-style: none;
  }
  .contact-list li { display: flex; align-items: center; gap: 10px; margin-top: 10px; font-size: 20px; }
  .contact-list li.contact-list__address { font-size: 14.5px; margin-top: 14px; }
  .icon { flex: none; fill: var(--ink); }
</style>
</head>
<body>
<main class="canvas">
  <section class="card card--back" aria-label="Card back">
    <div class="brand">
      <span class="brand__dot"></span>
      <span class="brand__name">HARLOW ESTATES</span>
    </div>
  </section>

  <section class="card card--front" aria-label="Card front">
    <div class="portrait" role="img" aria-label="Photo of the agent standing in front of a harbour marina"></div>
    <div class="details">
      <p class="details__name">Tom Harlow</p>
      <p class="details__phone">
        <svg class="icon" width="14" height="24" viewBox="0 0 14 24"><rect x="1" y="1" width="12" height="22" rx="2" fill="none" stroke="#1d1d1d" stroke-width="2"/><rect x="5" y="18" width="4" height="2"/></svg>
        0437 216 590
      </p>
      <ul class="contact-list">
        <li>
          <svg class="icon" width="20" height="14" viewBox="0 0 20 14"><rect width="20" height="14"/><path d="M0 0 L10 8 L20 0" fill="none" stroke="#fff" stroke-width="1.5"/></svg>
          tom@harlowestates.com.au
        </li>
        <li>
          <svg class="icon" width="20" height="20" viewBox="0 0 20 20"><circle cx="10" cy="10" r="9"/><path d="M2 10h16M10 1c-4 4-4 14 0 18M10 1c4 4 4 14 0 18" fill="none" stroke="#fff" stroke-width="1.3"/></svg>
          www.harlowestates.com.au
        </li>
        <li class="contact-list__address">
          <svg class="icon" width="16" height="22" viewBox="0 0 16 22"><path d="M8 0a8 8 0 0 0-8 8c0 6 8 14 8 14s8-8 8-14a8 8 0 0 0-8-8z"/><circle cx="8" cy="8" r="3" fill="#fff"/></svg>
          Level 2, 17 Kestrel Rd, Wendale NSW 2081
        </li>
      </ul>
    </div>
  </section>
</main>
</body>
</html>
```